IT Professional business card with a hometown feel and a little edgy.

My business name is Tamble Website Solutions. But I have ended up doing much more. I live in a very small remote community, where everyone knows everyone. We like the one-on-one customer service in this community. I do computer tutoring, virus removal, networking, and software training. My clients are businesses and private individuals.

My website is tamblewebsitesolutions.example, when I first designed it I was going for a fresh, clean look, which I still like. But I am thinking about making the website a bit more edgy to match my new logo from ArtHively (logo attached). At this time my website does not display the new logo, but I plan on redesigning the website in the future to match the logo and business card.

My tag line is "let the web work hard for you"

I'm thinking I would like to have the business card printed with a metallic finish.
Updates

Please do not use black backgrounds, or any solid dark colors. Prefer light or white backgrounds.

Target Market(s)

Small businesses. Individuals that need computer help at home.

Industry/Entity Type

It Company

Contact Information for Business Card

Nora Prandell
Tamble Website Solutions
PO Box 7153
Lindale, WA 98760
Cell: 555-271-3096
nora@tamblewebsitesolutions.example
tamblewebsitesolutions.example

Font styles to use
Serif

Requirements
Must have
• Must have all the information listed in "Business Card Details"
• Must use the logo provided.
• Use the colors from the provided logo
Nice to have
• Would like to use my tagline "let the web work hard for you" all lowercase

```html
<!DOCTYPE html>
<html lang="en">
<head>
<meta charset="utf-8">
<title>Tamble Website Solutions – Business Card</title>
<link rel="stylesheet" href="https://fonts.googleapis.com/css2?family=Source+Sans+3:ital,wght@0,400;0,600;1,600&display=swap">
<style>
  :root {
    --stage: #000000;
    --card: #ffffff;
    --brand-green: #3b7a2e;
    --ink: #1e1e1e;
    --ink-soft: #333333;
    --rule: #555555;
  }
  * { margin: 0; padding: 0; box-sizing: border-box; }
  html, body {
    width: 1200px; height: 900px; overflow: hidden;
    background: var(--stage);
    font-family: "Source Sans 3", "Myriad Pro", Arial, sans-serif;
  }
  .stage { position: relative; width: 1200px; height: 900px; }
  .card {
    position: absolute; width: 477px; height: 294px;
    background: var(--card);
  }
  .card--front { left: 116px; top: 275px; }
  .card--back { left: 622px; top: 276px; }

  .wordmark {
    position: absolute; display: flex; align-items: center;
    color: var(--brand-green); font-weight: 400;
  }
  .wordmark__square { background: var(--brand-green); flex: none; }
  .wordmark__divider { align-self: stretch; width: 1px; background: var(--rule); flex: none; }
  .card--front .wordmark { left: 136px; top: 65px; height: 102px; font-size: 17px; line-height: 17.5px; }
  .card--front .wordmark__square { width: 20px; height: 20px; margin-right: 28px; }
  .card--front .wordmark__divider { margin-right: 12px; }
  .card--back .wordmark { left: 223px; top: 74px; height: 117px; font-size: 20px; line-height: 20px; }
  .card--back .wordmark__square { width: 24px; height: 24px; margin-right: 28px; }
  .card--back .wordmark__divider { margin-right: 14px; }

  .holder-name {
    position: absolute; right: 22px; top: 24px;
    font-size: 19px; font-weight: 600; color: var(--brand-green);
  }
  .address {
    position: absolute; right: 22px; top: 161px;
    font-size: 14px; line-height: 20px; color: var(--ink);
    text-align: right; font-style: normal;
  }
  .contacts {
    position: absolute; right: 23px; top: 217px;
    list-style: none; font-size: 14px; color: var(--ink);
  }
  .contacts li {
    display: flex; justify-content: flex-end; align-items: center;
    gap: 7px; height: 19.5px;
  }
  .contacts svg { width: 14px; height: 14px; flex: none; }

  .tagline {
    position: absolute; left: 0; right: 0; top: 222px;
    text-align: center; font-size: 17px; font-weight: 600;
    font-style: italic; color: var(--ink-soft);
  }
</style>
</head>
<body>
<main class="stage">
  <section class="card card--front">
    <p class="holder-name">Nora Prandell</p>
    <div class="wordmark">
      <span class="wordmark__square"></span>
      <span class="wordmark__divider"></span>
      <span>Tamble<br>Website<br>Solutions</span>
    </div>
    <address class="address">PO Box 7153<br>Lindale, WA 98760</address>
    <ul class="contacts">
      <li>555-271-3096
        <svg viewBox="0 0 14 14" aria-hidden="true"><rect width="14" height="14" rx="2" fill="#3b7a2e"/><path d="M3 5.2c0-1 .9-1.6 4-1.6s4 .6 4 1.6v.6H9.4v-.8H4.6v.8H3z M4.2 6.6h5.6l.8 3.8H3.4z" fill="#fff"/></svg>
      </li>
      <li>nora@tamblewebsitesolutions.example
        <svg viewBox="0 0 14 14" aria-hidden="true"><rect width="14" height="14" rx="2" fill="#3b7a2e"/><rect x="3" y="4" width="8" height="6" fill="#fff"/><path d="M3 4l4 3.2L11 4" stroke="#3b7a2e" stroke-width="1" fill="none"/></svg>
      </li>
      <li>www.tamblewebsitesolutions.example
        <svg viewBox="0 0 14 14" aria-hidden="true"><rect width="14" height="14" rx="2" fill="#3b7a2e"/><path d="M6 8.2l2.2-2.2M5 6.8L3.8 8a1.5 1.5 0 002.2 2.2L7.2 9M9 7.2L10.2 6A1.5 1.5 0 008 3.8L6.8 5" stroke="#fff" stroke-width="1.3" fill="none" stroke-linecap="round"/></svg>
      </li>
    </ul>
  </section>

  <section class="card card--back">
    <div class="wordmark">
      <span class="wordmark__square"></span>
      <span class="wordmark__divider"></span>
      <span>Tamble<br>Website<br>Solutions</span>
    </div>
    <p class="tagline">"let the web work hard for you"</p>
  </section>
</main>
</body>
</html>
```